Velmora health leaflet

We are looking for a new brand identity for our clinic to start with a new leaflet for communication. For current brand identity please look at our website Www.velmorahealth.cz. We would like to use less of the blue but more of the green turquoise and white. The logo should remain. See attached. We received few ideas but not sure about them. The design should be elegant and simple. Premium
#729694 Hex Color Code
The hexadecimal color code #729694 is a shade of cyan. In the RGB color model #729694 is composed of 44.71% red, 58.82% green and 58.04% blue. In the HSL color space #729694 has a hue of 177° (degrees), 15% saturation and 52% lightness. This color has an approximate wavelength of 492.66 nm.
Main headlines
Playfair Display
Serif, elegant
Body & UI
Lato
Clean, modern
Look and feel
Each slider illustrates characteristics of the customer's brand and the style your logo design should communicate.

```html
<!DOCTYPE html>
<html lang="en">
<head>
<meta charset="utf-8">
<title>Velmora Health Leaflet</title>
<link rel="stylesheet" href="https://fonts.googleapis.com/css2?family=Playfair+Display:wght@400;500&family=Crimson+Text:ital@0;1&family=Lato:wght@400&display=swap">
<style>
  :root {
    --board: #86b4aa;
    --paper: #ffffff;
    --paper-mid: #f1f2f2;
    --teal: #6aa796;
    --ink: #2f3535;
    --ink-soft: #5a6262;
    --white: #ffffff;
  }
  * { margin: 0; padding: 0; box-sizing: border-box; }
  html, body { width: 1200px; height: 1200px; overflow: hidden; }
  body { background: var(--board); position: relative; font-family: "Crimson Text", Georgia, serif; color: var(--ink); }

  .board-title {
    position: absolute; top: 112px; left: 0; width: 1200px; text-align: center;
    font-family: "Playfair Display", Georgia, serif; font-weight: 400;
    font-size: 60px; letter-spacing: 2px; color: var(--white);
  }
  .board-url {
    position: absolute; top: 194px; left: 0; width: 1200px; text-align: center;
    font-family: "Crimson Text", Georgia, serif; font-size: 33px; color: var(--white);
  }
  .board-caption {
    position: absolute; top: 1016px; left: 0; width: 1200px; text-align: center;
    font-family: "Lato", Arial, sans-serif; font-size: 34px; letter-spacing: 1px; color: var(--white);
  }
  .board-region {
    position: absolute; top: 1058px; left: 0; width: 1200px; text-align: center;
    font-family: "Crimson Text", Georgia, serif; font-size: 36px; color: var(--white);
  }

  .leaflet {
    position: absolute; left: 260px; top: 349px; width: 678px; height: 539px;
    display: flex; background: var(--paper);
    box-shadow: 12px 14px 26px rgba(40, 80, 72, 0.22);
  }
  .panel { position: relative; width: 226px; height: 100%; }
  .panel--middle { background: var(--paper-mid); }

  .brand-name {
    position: absolute; left: 0; width: 100%; text-align: center;
    font-family: "Crimson Text", Georgia, serif; font-size: 19px; color: var(--ink);
  }
  .brand-name::before {
    content: ""; display: inline-block; width: 8px; height: 8px; border-radius: 50%;
    background: var(--teal); margin-right: 6px; vertical-align: middle;
  }
  .cover-title {
    position: absolute; top: 136px; left: 0; width: 100%; text-align: center;
    font-family: "Playfair Display", Georgia, serif; font-size: 25px; line-height: 29px; color: var(--ink);
  }
  .cover-tagline {
    position: absolute; top: 196px; left: 0; width: 100%; text-align: center;
    font-style: italic; font-size: 13px; color: var(--ink-soft);
  }
  .section-heading {
    position: absolute; left: 0; width: 100%; text-align: center;
    font-family: "Playfair Display", Georgia, serif; font-size: 15px; line-height: 20px;
    color: var(--teal); letter-spacing: 0.3px;
  }
  .section-body {
    position: absolute; left: 28px; width: 170px; text-align: center;
    font-size: 11.5px; line-height: 14px; color: var(--ink-soft);
  }
  .feature {
    position: absolute; display: flex; align-items: center; gap: 9px;
    font-size: 13px; color: var(--ink);
  }
  .feature svg { width: 19px; height: 19px; flex: none; }
  .availability {
    position: absolute; top: 228px; left: 0; width: 100%; text-align: center; font-size: 13.5px;
  }
  .contact {
    position: absolute; left: 0; width: 100%; text-align: center;
    font-family: "Lato", Arial, sans-serif; font-size: 8.5px; color: var(--ink-soft);
  }
  .social-row {
    position: absolute; top: 476px; left: 0; width: 100%;
    display: flex; justify-content: center; gap: 10px;
  }
  .social-dot { width: 18px; height: 18px; border-radius: 50%; background: var(--teal); }
  .panel-band { position: absolute; left: 0; bottom: 0; width: 100%; height: 16px; background: var(--teal); }
</style>
</head>
<body>
  <h1 class="board-title">VELMORA HEALTH</h1>
  <p class="board-url">www.velmorahealth.cz</p>

  <div class="leaflet">
    <section class="panel panel--cover">
      <div class="brand-name" style="top:78px;">Velmora Health</div>
      <h2 class="cover-title">VELMORA<br>HEALTH</h2>
      <p class="cover-tagline">Transforming healthcare</p>
      <h3 class="section-heading" style="top:283px;">OUR PHILOSOPHY</h3>
      <p class="section-body" style="top:313px;">We believe care should be personal, unhurried and close at hand, with one physician who knows your story and guides every decision with you.</p>
    </section>

    <section class="panel panel--middle">
      <h3 class="section-heading" style="top:154px;">BESPOKE HEALTH</h3>
      <p class="section-body" style="top:190px;">Each plan is shaped around your life, your goals and your time, with care that reaches well beyond the clinic.</p>
      <div class="feature" style="top:284px; left:39px;">
        <svg viewBox="0 0 20 20"><path d="M10 2 L16.5 4.5 V9.5 C16.5 13.5 13.5 16.5 10 18 C6.5 16.5 3.5 13.5 3.5 9.5 V4.5 Z" fill="none" stroke="var(--teal)" stroke-width="1.5"/><path d="M10 5 L14 6.6 V9.7 C14 12.2 12.2 14.2 10 15.2 Z" fill="var(--teal)"/></svg>
        <span>Personalized Wellness</span>
      </div>
      <div class="feature" style="top:335px; left:39px;">
        <svg viewBox="0 0 20 20"><circle cx="10" cy="10" r="8" fill="none" stroke="var(--teal)" stroke-width="1.5"/><path d="M10 5.5 V10.5 L8.5 12.5" fill="none" stroke="var(--teal)" stroke-width="1.5" stroke-linecap="round"/></svg>
        <span>Proactive Health</span>
      </div>
    </section>

    <section class="panel panel--contact">
      <h3 class="section-heading" style="top:151px;">EXCLUSIVE<br>ACCESS</h3>
      <p class="availability">24/7 Availability</p>
      <div class="feature" style="top:265px; left:35px;">
        <svg viewBox="0 0 20 20"><path d="M10 2 L16.5 4.5 V9.5 C16.5 13.5 13.5 16.5 10 18 C6.5 16.5 3.5 13.5 3.5 9.5 V4.5 Z" fill="none" stroke="var(--teal)" stroke-width="1.5"/><path d="M10 5 L14 6.6 V9.7 C14 12.2 12.2 14.2 10 15.2 Z" fill="var(--teal)"/></svg>
        <span>Specialist Network</span>
      </div>
      <div class="feature" style="top:302px; left:35px;">
        <svg viewBox="0 0 20 20"><path d="M10 18 V8" stroke="var(--teal)" stroke-width="1.6" stroke-linecap="round"/><path d="M10 10 C10 6 13 4 16.5 4 C16.5 7.5 14 10 10 10 Z" fill="var(--teal)"/><path d="M10 12 C10 9.5 7.5 8 4.5 8 C4.5 10.5 6.5 12 10 12 Z" fill="var(--teal)"/><path d="M5 18 H15" stroke="var(--teal)" stroke-width="1.4" stroke-linecap="round"/></svg>
        <span>Advanced Diagnostics</span>
      </div>
      <div class="brand-name" style="top:400px; font-size:15px;">Velmora Health</div>
      <p class="contact" style="top:437px;">www.velmorahealth.cz</p>
      <p class="contact" style="top:449px;">Praha 1, Vodičkova 14</p>
      <div class="social-row">
        <span class="social-dot"></span><span class="social-dot"></span><span class="social-dot"></span><span class="social-dot"></span>
      </div>
      <div class="panel-band"></div>
    </section>
  </div>

  <p class="board-caption">INFOGRAPHIC DESIGN</p>
  <p class="board-region">Czech Republic</p>
</body>
</html>
```